" A empresa opera um ecossistema que conecta o transporte público a benefícios sociais, permitindo que usuários de cartões de transporte possam acessar serviços de saúde, descontos e recargas integradas por meio de um modelo digital de adesão e refiliação. "

```html
<!DOCTYPE html>
<html lang="pt-BR">
<head>
<meta charset="UTF-8">
<title>Quem move a cidade, move o coração da comunidade</title>
<link href="https://fonts.googleapis.com/css2?family=Montserrat:wght@400;500;700;800&display=swap" rel="stylesheet">
<style>
  :root {
    --paper: #ffffff;
    --navy: #122d42;
    --navy-deep: #0c2234;
    --teal: #2d97a3;
    --teal-light: #5ec3cd;
    --text: #e6eef3;
    --bus-light: #e9edf0;
    --bus-mid: #aeb7bf;
    --person-skin: #9a6a4c;
    --person-dark: #2a2a2c;
  }
  * { margin: 0; padding: 0; box-sizing: border-box; }
  html, body {
    width: 1200px; height: 1200px; overflow: hidden;
    background: var(--paper);
    font-family: 'Montserrat', Arial, sans-serif;
  }
  .canvas { position: relative; width: 1200px; height: 1200px; }
  .banner {
    position: absolute; left: 0; top: 264px; width: 1200px; height: 672px;
    background: linear-gradient(120deg, var(--navy-deep) 0%, var(--navy) 55%, #173a54 100%);
    overflow: hidden;
  }
  .accent-panel {
    position: absolute; left: 900px; top: 0; width: 300px; height: 380px;
    background: var(--teal);
  }
  .headline {
    position: absolute; left: 72px; top: 96px;
    font-weight: 800; font-size: 27px; line-height: 52px;
    letter-spacing: 2.5px; text-transform: uppercase;
  }
  .headline .lead { color: var(--teal-light); display: block; }
  .headline .strong { color: var(--paper); display: block; }
  .body-copy {
    position: absolute; left: 72px; top: 238px; width: 610px;
    color: var(--text); font-size: 16.5px; line-height: 27px; font-weight: 400;
  }
  .body-copy p + p { margin-top: 27px; }
  .rule {
    position: absolute; left: 72px; top: 610px; width: 480px; height: 13px;
    background: var(--teal);
  }
  .bus-photo {
    position: absolute; left: 684px; top: 72px; width: 516px; height: 326px;
    border-radius: 40px 0 0 28px;
    background: linear-gradient(160deg, var(--bus-light) 0%, #ffffff 40%, var(--bus-mid) 100%);
  }
  .person-photo {
    position: absolute; left: 756px; top: 204px; width: 350px; height: 468px;
    border-radius: 150px 150px 0 0;
    background: linear-gradient(180deg, var(--person-skin) 0%, #6e4a35 30%, var(--person-dark) 55%, #4a4a46 100%);
  }
</style>
</head>
<body>
<div class="canvas">
  <section class="banner">
    <div class="accent-panel"></div>
    <h1 class="headline">
      <span class="lead">Quem move a cidade, move</span>
      <span class="strong">o coração da comunidade</span>
    </h1>
    <div class="body-copy">
      <p>Através do transporte público circulam aqueles que ensinam a ler, escrever, calcular e milhões de pessoas que, todos os dias, ajudam a tornar as regiões metropolitanas cada vez melhores.</p>
      <p>Os meios de transporte público são essenciais para quem garante o nosso pão de cada dia e para milhões de cidadãos que constroem cidades mais fortes e humanas.</p>
      <p>São conduzidos por quem nos recebe com um sorriso no rosto e faz de tudo para atender as necessidades de milhões de pessoas em suas comunidades.</p>
    </div>
    <div class="rule"></div>
    <div class="bus-photo" role="img" aria-label="Foto de um ônibus urbano branco visto de frente em diagonal"></div>
    <div class="person-photo" role="img" aria-label="Foto de um homem sorridente de camisa listrada e mochila, segurando um cartão de transporte"></div>
  </section>
</div>
</body>
</html>
```